Ridgeline Outfitters Business Cards

Recently had a logo done with Artfolio and now looking for a business card to go along with it.

Target Market(s)

Ridgeline Outfitters is a weapons dealer. My market will be primarily men, hunting, shooting type.

Industry/Entity Type

Business

Contact Information for Business Card

I selected double sided, but this is not required, single or double is going to be fine. I picture the logo on one side, or perhaps just the circle which contains "RO" with the remaining info on the other side.

Font styles to use
Sans Serif

Requirements
Must have
• My name: Milo Brandt
• Title: Owner
• tel: 612-555-0187
• web: www.ridgelineoutfittersmn.example
Nice to have
• I like the concept of a black business card. I would like to keep the colors monotone, black, grey, white or red. Red is acceptable because it is in the logo. I have also seen cards that are matte black with shiny black as well, perhaps for the logo (or circle RO) part of the logo.
• I will upload a couple of the logos for use, and also an example I just found of the black on black. and some others that have a nice contrast.
Should not have
• lots of colors are not wanted.

```html
<!DOCTYPE html>
<html lang="en">
<head>
<meta charset="utf-8">
<title>Ridgeline Outfitters – Business Card Options</title>
<link href="https://fonts.googleapis.com/css2?family=Oswald:wght@600&family=Abel&family=Fjalla+One&family=Roboto:wght@300&display=swap" rel="stylesheet">
<style>
  :root {
    --page: #ece6dc;
    --ink: #2b2b2b;
    --card-black: #000000;
    --brand-red: #e0232b;
    --text-white: #ffffff;
    --silver-light: #ffffff;
    --silver-mid: #d6d6d6;
    --silver-dark: #9a9a9a;
  }
  * { box-sizing: border-box; margin: 0; padding: 0; }
  html, body { width: 1005px; height: 1200px; overflow: hidden; }
  body { background: var(--page); position: relative; font-family: "Abel", sans-serif; }

  .sheet-label {
    position: absolute; top: 40px; left: 0; width: 1047px; text-align: center;
    font-family: "Roboto", sans-serif; font-weight: 300; font-size: 38px; color: var(--ink);
  }
  .option-number {
    position: absolute; left: 56px; font-family: "Roboto", sans-serif; font-weight: 300;
    font-size: 62px; color: var(--ink);
  }
  .option-number.first { top: 345px; }
  .option-number.second { top: 838px; }

  .card {
    position: absolute; left: 131px; width: 754px; height: 437px;
    background: var(--card-black); overflow: hidden;
    box-shadow: 0 3px 10px rgba(0,0,0,.25);
  }
  .card.option-one { top: 140px; }
  .card.option-two { top: 645px; left: 129px; background: transparent; }

  .silver-field {
    position: absolute; inset: 0;
    background: linear-gradient(100deg, var(--silver-mid) 0%, var(--silver-light) 45%, var(--silver-light) 60%, var(--silver-dark) 100%);
  }
  .black-sweep { position: absolute; left: 0; top: 0; width: 754px; height: 437px; }

  .brand-name {
    position: absolute;
    font-family: "Oswald", sans-serif; font-weight: 600; font-size: 40px;
    letter-spacing: 1px; text-transform: uppercase; color: var(--brand-red); white-space: nowrap;
  }
  .option-one .brand-name { left: 268px; top: 105px; }
  .option-two .brand-name { left: 266px; top: 60px; }

  .holder {
    position: absolute; top: 272px; right: 493px; text-align: right; color: var(--text-white);
  }
  .holder-name { font-family: "Fjalla One", sans-serif; font-size: 25px; line-height: 1.2; }
  .holder-title { font-family: "Abel", sans-serif; font-size: 24px; line-height: 1.3; }

  .divider {
    position: absolute; left: 301px; top: 230px; width: 4px; height: 159px; background: var(--brand-red);
  }

  .contact-list { position: absolute; left: 330px; top: 258px; list-style: none; }
  .contact-list li {
    display: flex; align-items: center; height: 38px; gap: 10px;
    font-size: 24px; color: var(--text-white); white-space: nowrap;
  }
  .contact-list svg { width: 20px; height: 20px; flex: none; }
</style>
</head>
<body>
  <div class="sheet-label">one-sided</div>
  <div class="option-number first">1</div>
  <div class="option-number second">2</div>

  <section class="card option-one">
    <div class="brand-name">Ridgeline Outfitters</div>
    <div class="holder">
      <div class="holder-name">Milo Brandt</div>
      <div class="holder-title">Owner</div>
    </div>
    <div class="divider"></div>
    <ul class="contact-list">
      <li><svg viewBox="0 0 20 20"><rect x="5" y="1" width="10" height="18" rx="2" fill="none" stroke="#e0232b" stroke-width="1.8"/><line x1="8" y1="16" x2="12" y2="16" stroke="#e0232b" stroke-width="1.5"/></svg>612-555-0187</li>
      <li><svg viewBox="0 0 20 20"><rect x="1" y="4" width="18" height="12" fill="none" stroke="#e0232b" stroke-width="1.8"/><polyline points="1,4 10,11 19,4" fill="none" stroke="#e0232b" stroke-width="1.5"/></svg>milo@ridgelineoutfittersmn.example</li>
      <li><svg viewBox="0 0 20 20"><circle cx="10" cy="10" r="8.5" fill="none" stroke="#e0232b" stroke-width="1.6"/><ellipse cx="10" cy="10" rx="4" ry="8.5" fill="none" stroke="#e0232b" stroke-width="1.3"/><line x1="1.5" y1="10" x2="18.5" y2="10" stroke="#e0232b" stroke-width="1.3"/></svg>www.ridgelineoutfittersmn.example</li>
    </ul>
  </section>

  <section class="card option-two">
    <div class="silver-field"></div>
    <svg class="black-sweep" viewBox="0 0 754 437" preserveAspectRatio="none" aria-hidden="true">
      <defs>
        <linearGradient id="sweep-edge" x1="0" x2="1" y1="0" y2="0">
          <stop offset="0" stop-color="#8c8c8c"/>
          <stop offset="0.5" stop-color="#e8e8e8"/>
          <stop offset="1" stop-color="#7a7a7a"/>
        </linearGradient>
      </defs>
      <path d="M0 216 Q377 182 754 206 L754 437 L0 437 Z" fill="url(#sweep-edge)"/>
      <path d="M0 227 Q377 190 754 216 L754 437 L0 437 Z" fill="#000"/>
    </svg>
    <div class="brand-name">Ridgeline Outfitters</div>
    <div class="holder">
      <div class="holder-name">Milo Brandt</div>
      <div class="holder-title">Owner</div>
    </div>
    <div class="divider"></div>
    <ul class="contact-list">
      <li><svg viewBox="0 0 20 20"><rect x="5" y="1" width="10" height="18" rx="2" fill="none" stroke="#e0232b" stroke-width="1.8"/><line x1="8" y1="16" x2="12" y2="16" stroke="#e0232b" stroke-width="1.5"/></svg>612-555-0187</li>
      <li><svg viewBox="0 0 20 20"><rect x="1" y="4" width="18" height="12" fill="none" stroke="#e0232b" stroke-width="1.8"/><polyline points="1,4 10,11 19,4" fill="none" stroke="#e0232b" stroke-width="1.5"/></svg>milo@ridgelineoutfittersmn.example</li>
      <li><svg viewBox="0 0 20 20"><circle cx="10" cy="10" r="8.5" fill="none" stroke="#e0232b" stroke-width="1.6"/><ellipse cx="10" cy="10" rx="4" ry="8.5" fill="none" stroke="#e0232b" stroke-width="1.3"/><line x1="1.5" y1="10" x2="18.5" y2="10" stroke="#e0232b" stroke-width="1.3"/></svg>www.ridgelineoutfittersmn.example</li>
    </ul>
  </section>
</body>
</html>
```